Business Card and Letterhead Design for Public Accounting Firm

Business card and letterhead design for a CPA Firm located in Orange County, CA. We're looking for a modern and professional design utilizing our existing logo. We'd like a clean "less is more" look, but also something that catches the eye. We provide a high level of service to our clients. Open to single or double sided business cards.

Additional info: color numbers on logo
Blue :
R 0
G 83
B 125

#00537D

Silver :

R 154
G 154
B 154

#9A9A9A

Target Market(s)

Businesses and individuals

Industry/Entity Type

Accounting

Contact Information for Business Card

Moss Whitfield & Danby LLP - 4827 Larkspur Vale Road, Irvine, CA 92614 - (949)731-2864 - mwdaccts.example

Font styles to use
Serif
Sans Serif
Other font styles liked:
• See font file uploaded

Colors
0054AA
0677BA
7BADD7
CADEEF
E8F1F8

Requirements
Nice to have
• Possibly use the font file provided which matches our logo, but adjust to be not in all caps

```html
<!DOCTYPE html>
<html lang="en">
<head>
<meta charset="utf-8">
<title>Moss Whitfield &amp; Danby LLP — Business Card</title>
<link rel="stylesheet" href="https://fonts.googleapis.com/css2?family=Cinzel:wght@500&family=Montserrat:wght@600;700&family=Roboto:wght@400&display=swap">
<style>
  :root {
    --brand-blue: #00537d;
    --brand-silver: #9a9a9a;
    --text-grey: #7a7a7a;
    --card-white: #f7f7f7;
    --backdrop: #e9e7e4;
  }
  * { box-sizing: border-box; margin: 0; padding: 0; }
  html, body { width: 1200px; height: 900px; overflow: hidden; }
  body { background: var(--backdrop); position: relative; }

  .card {
    position: absolute;
    top: 296px;
    width: 540px;
    height: 309px;
    background: var(--card-white);
    box-shadow: 0 10px 28px rgba(0,0,0,.14);
    overflow: hidden;
  }
  .card::after {
    content: "";
    position: absolute;
    left: 0; right: 0; bottom: 0;
    height: 9px;
    background: var(--brand-blue);
  }
  .card--contact { left: 40px; }
  .card--brand { left: 620px; }

  /* contact side */
  .firm-name {
    position: absolute;
    right: 34px; top: 34px;
    font-family: "Cinzel", serif;
    font-weight: 500;
    font-size: 19px;
    color: var(--brand-blue);
    text-align: right;
    line-height: 1.25;
  }
  .rule {
    position: absolute;
    left: 34px; right: 34px; top: 160px;
    height: 1px;
    background: var(--brand-blue);
  }
  .person {
    position: absolute;
    left: 34px; top: 112px;
    font-family: "Montserrat", sans-serif;
    color: var(--brand-blue);
  }
  .person__name { font-weight: 700; font-size: 21px; letter-spacing: .5px; line-height: 1; }
  .person__title { font-weight: 600; font-size: 14px; margin-top: 4px; }

  .contact-list {
    position: absolute;
    left: 34px; top: 184px;
    list-style: none;
    font-family: "Roboto", sans-serif;
    font-size: 12.5px;
    color: var(--text-grey);
  }
  .contact-list li { display: flex; align-items: center; gap: 10px; height: 24px; }
  .contact-list svg { width: 15px; height: 15px; fill: var(--brand-blue); flex: none; }

  .address {
    position: absolute;
    right: 34px; top: 176px;
    font-family: "Roboto", sans-serif;
    font-size: 12.5px;
    line-height: 1.45;
    color: var(--text-grey);
    text-align: right;
  }
  .address svg { width: 13px; height: 16px; fill: var(--brand-blue); display: block; margin: 0 0 4px auto; }

  /* brand side */
  .brand-lockup {
    position: absolute;
    inset: 0 0 9px 0;
    display: flex;
    align-items: center;
    justify-content: center;
    gap: 18px;
  }
  .brand-lockup__mark {
    width: 22px; height: 22px;
    background: var(--brand-blue);
  }
  .brand-lockup__name {
    font-family: "Cinzel", serif;
    font-weight: 500;
    font-size: 27px;
    letter-spacing: 2px;
    line-height: 1.2;
    color: var(--brand-silver);
  }
</style>
</head>
<body>

<section class="card card--contact">
  <p class="firm-name">Moss Whitfield<br>&amp; Danby LLP</p>

  <div class="person">
    <p class="person__name">YOUR NAME</p>
    <p class="person__title">your title</p>
  </div>

  <div class="rule"></div>

  <ul class="contact-list">
    <li>
      <svg viewBox="0 0 24 24" aria-hidden="true"><path d="M6.6 10.8a15.1 15.1 0 0 0 6.6 6.6l2.2-2.2a1 1 0 0 1 1-.25 11.4 11.4 0 0 0 3.6.57 1 1 0 0 1 1 1V20a1 1 0 0 1-1 1A17 17 0 0 1 3 4a1 1 0 0 1 1-1h3.5a1 1 0 0 1 1 1c0 1.25.2 2.45.57 3.57a1 1 0 0 1-.25 1z"/></svg>
      (949)731-2864
    </li>
    <li>
      <svg viewBox="0 0 24 24" aria-hidden="true"><path d="M2 5h20v14H2zm2 2v.4l8 5.2 8-5.2V7zm0 2.8V17h16V9.8l-8 5.2z"/></svg>
      office@mwdaccts.example
    </li>
    <li>
      <svg viewBox="0 0 24 24" aria-hidden="true"><path d="M12 2a10 10 0 1 0 0 20 10 10 0 0 0 0-20zm6.9 6h-3a15.6 15.6 0 0 0-1.3-3.8A8 8 0 0 1 18.9 8zM12 4c.8 1.2 1.5 2.5 1.9 4h-3.8c.4-1.5 1.1-2.8 1.9-4zM4.3 14a8 8 0 0 1 0-4h3.4a16.5 16.5 0 0 0 0 4zm.8 2h3a15.6 15.6 0 0 0 1.3 3.8A8 8 0 0 1 5.1 16zM8 8H5.1a8 8 0 0 1 4.3-3.8A15.6 15.6 0 0 0 8 8zm4 12c-.8-1.2-1.5-2.5-1.9-4h3.8c-.4 1.5-1.1 2.8-1.9 4zm2.3-6H9.7a14.7 14.7 0 0 1 0-4h4.6a14.7 14.7 0 0 1 0 4zm.3 5.8A15.6 15.6 0 0 0 16 16h2.9a8 8 0 0 1-4.3 3.8zM16.3 14a16.5 16.5 0 0 0 0-4h3.4a8 8 0 0 1 0 4z"/></svg>
      www.mwdaccts.example
    </li>
  </ul>

  <div class="address">
    <svg viewBox="0 0 16 20" aria-hidden="true"><path d="M8 0a7 7 0 0 0-7 7c0 5 7 13 7 13s7-8 7-13a7 7 0 0 0-7-7zm0 9.6A2.6 2.6 0 1 1 8 4.4a2.6 2.6 0 0 1 0 5.2z"/></svg>
    4827 Larkspur Vale Road<br>Irvine, CA 92614
  </div>
</section>

<section class="card card--brand">
  <div class="brand-lockup">
    <span class="brand-lockup__mark" aria-hidden="true"></span>
    <p class="brand-lockup__name">Moss Whitfield<br>&amp; Danby LLP</p>
  </div>
</section>

</body>
</html>
```